Brand Packaging Identity H
ZOLT WATCHES
Dear Designers,
Thanks everyone for there contribution and efforts, we shall finalize the project in a day.
Many thanks once again,
Regards,
PH
Thank you
have you decided yet?
LAST 2 days to go...
Goodluck,
The project has been extended for 4 days more, please understand our requirements and post your drafts.
Thanks,
#90 Please use original brand identity in your designs.
The project has been extended for 4 days, please submit your designs and we hope you'll meet the expectations.
Thank you all for your efforts, the contest will be over in next 10 hours. Please recharge your enthusiasm and strike your new ideas in new designs.
All the best,
Please be different in Watch Gift Box designing and Watch Tags designing, its not just an identical design on every item but its about creating new standards and new styles for a better usage. So, please be creative and innovative, all submitted drafts have almost similar stuff with a difference in design and art. Please add new and fresh ideas.
All goodluck, JUST ONE DAY TO GO.
Come'on Designers Buck up, its just 2 days more... send your designs and get over it.
#49: Please use the exact identity in your designs and instead of black gray could be a nicer combination.
Also try in another design combination near to the requirements.
#64: One star for the watch Pad and polybag, other identities could be much better please make it more appealing.
Rgds.,
#67: Zolt is a trendy digital watch, we appreciate your efforts, could be better.
the project has been extended for 3 days, please submit your designs soon.
Hello Ph,
Please check your private message at upper right corner.
#50: Zolt is a trendy digital watch.
Please be innovative in your work, there could be much better designs that draws better impact to the mind and leaves a lasting impression. Please submit those designs.
JUST A DAY TO GO...
Goodluck ALL,
#43: made it so simple, please be unique remember its a trendy digital watch, fresh ideas will be appreciated.
#44: You are a bit creative, but please use light colors in your designs, we value your efforts.
#45: We are looking for light color identity, your designs are good but would be much better if light background was used.
lets be active and make your creativity and concepts flow in designs.
Goodluck everyone,
rgds.,
The project has been extended for 3 days, please submit your fresh designs soon.

```html
<!DOCTYPE html>
<html lang="en">
<head>
<meta charset="utf-8">
<title>Zolt Watches – Gift Box and Tag Set</title>
<link rel="stylesheet" href="https://fonts.googleapis.com/css2?family=Arimo:wght@400;700&display=swap">
<style>
  :root {
    --bg: #dcdcdc;
    --blue: #1f5aa8;
    --blue-deep: #134385;
    --blue-light: #3f7fcc;
    --white: #ffffff;
    --fold: rgba(255,255,255,0.35);
    --cell-line: #6f8fbf;
  }
  * { margin: 0; padding: 0; box-sizing: border-box; }
  html, body { width: 1200px; height: 871px; overflow: hidden; }
  body {
    background: var(--bg);
    font-family: "Arimo", Arial, sans-serif;
    color: var(--white);
    position: relative;
  }
  .piece {
    position: absolute;
    background: linear-gradient(180deg, var(--blue) 0%, var(--blue-deep) 100%);
    overflow: hidden;
  }
  .piece.fold { outline: 1px solid var(--fold); outline-offset: -1px; }
  .dial-art {
    position: absolute;
    background: radial-gradient(circle at 50% 50%, rgba(120,170,235,0.35) 0%, rgba(90,140,215,0.18) 45%, rgba(31,90,168,0) 70%);
  }
  .brand {
    position: absolute;
    font-weight: 700;
    letter-spacing: 1px;
    color: var(--white);
    line-height: 1;
    text-transform: lowercase;
    white-space: nowrap;
  }
  .slogan {
    position: absolute;
    font-size: 13px;
    letter-spacing: 3px;
    text-transform: uppercase;
    color: var(--white);
    white-space: nowrap;
    line-height: 1;
  }
  .web {
    position: absolute;
    font-size: 22px;
    font-weight: 700;
    color: var(--white);
    white-space: nowrap;
  }
  .spec-table {
    position: absolute;
    display: grid;
    grid-template-columns: repeat(5, 1fr);
    grid-template-rows: 14px 1fr;
    gap: 0 3px;
  }
  .spec-table .head {
    font-size: 6px;
    text-align: center;
    line-height: 14px;
    color: var(--white);
    white-space: nowrap;
  }
  .spec-table .cell {
    background: var(--white);
    border: 1px solid var(--cell-line);
  }
</style>
</head>
<body>

  <section class="gift-box">
    <div class="piece fold top-flap" style="left:192px; top:120px; width:300px; height:91px;">
      <div class="dial-art" role="img" aria-label="Faint watch dial decoration" style="left:0; top:-40px; width:300px; height:160px;"></div>
      <div class="slogan" style="left:50%; top:28px; transform:translateX(-50%) rotate(180deg);">Own Every Second</div>
    </div>

    <div class="piece fold side-left" style="left:132px; top:211px; width:60px; height:473px;">
      <div class="dial-art" role="img" aria-label="Faint watch dial decoration" style="left:-40px; top:20px; width:140px; height:200px;"></div>
      <div class="slogan" style="font-size:8px; letter-spacing:1px; transform:rotate(90deg); transform-origin:left top; left:44px; top:62px;">Own Every Second</div>
      <div class="brand" style="font-size:30px; transform:rotate(90deg); transform-origin:left top; left:48px; top:360px;">zolt</div>
    </div>

    <div class="piece fold front-panel" style="left:192px; top:211px; width:300px; height:473px; background:radial-gradient(ellipse at 50% 40%, var(--blue-light) 0%, var(--blue) 45%, var(--blue-deep) 100%);">
      <div class="dial-art" role="img" aria-label="Large watch dial illustration" style="left:0; top:140px; width:300px; height:300px;"></div>
      <div class="brand" style="left:0; width:100%; text-align:center; top:24px; font-size:42px;">zolt</div>
      <div class="slogan" style="left:50%; top:72px; transform:translateX(-50%); font-size:7px; letter-spacing:2px;">Own Every Second</div>
      <div class="web" style="left:50%; top:423px; transform:translateX(-50%);">www.zoltdomain.com</div>
    </div>

    <div class="piece fold side-right" style="left:492px; top:211px; width:60px; height:473px;">
      <div class="dial-art" role="img" aria-label="Faint watch dial decoration" style="left:-60px; top:120px; width:140px; height:240px;"></div>
      <div class="brand" style="font-size:20px; transform:rotate(-90deg); transform-origin:left top; left:20px; top:62px;">zolt</div>
    </div>

    <div class="piece fold bottom-flap" style="left:192px; top:684px; width:300px; height:79px;">
      <div class="spec-table" style="left:12px; top:6px; width:276px; height:48px;">
        <div class="head">Model No</div><div class="head">Case Color</div><div class="head">Band Color</div><div class="head">Dial Color</div><div class="head">Quantity</div>
        <div class="cell"></div><div class="cell"></div><div class="cell"></div><div class="cell"></div><div class="cell"></div>
      </div>
    </div>
  </section>

  <section class="watch-tags">
    <div class="piece tag-slogan" style="left:811px; top:242px; width:317px; height:72px;">
      <div class="dial-art" role="img" aria-label="Faint watch dial decoration" style="left:180px; top:-40px; width:160px; height:150px;"></div>
      <div class="slogan" style="left:50%; top:29px; transform:translateX(-50%);">Own Every Second</div>
    </div>

    <div class="piece tag-spec" style="left:811px; top:350px; width:317px; height:70px;">
      <div class="spec-table" style="left:20px; top:5px; width:277px; height:56px;">
        <div class="head">Model No</div><div class="head">Case Color</div><div class="head">Band Color</div><div class="head">Dial Color</div><div class="head">Quantity</div>
        <div class="cell"></div><div class="cell"></div><div class="cell"></div><div class="cell"></div><div class="cell"></div>
      </div>
    </div>

    <div class="piece tag-brand" style="left:643px; top:449px; width:485px; height:77px;">
      <div class="dial-art" role="img" aria-label="Watch dial illustration" style="left:0; top:-60px; width:300px; height:200px;"></div>
      <div class="brand" style="right:44px; top:26px; font-size:24px;">zolt</div>
    </div>

    <div class="piece tag-brand" style="left:643px; top:550px; width:485px; height:79px;">
      <div class="dial-art" role="img" aria-label="Watch dial illustration" style="left:120px; top:-60px; width:300px; height:200px;"></div>
      <div class="brand" style="right:44px; top:27px; font-size:24px;">zolt</div>
    </div>
  </section>

</body>
</html>
```